Kessalt Orthodontics
Stationary, Business Card, Appointment Card, Envelope, Folder
Project: Kessalt Orthodontics
Kessalt Orthodontics - Health
Creative Brief
Professional
Marcus Kessalt, DMD
4183 Harlow Crest Dr., #210 Marlow Bay, CA 95871 6452 Bramwell-Tusk Rd., #B Ashford Glen, CA 95683
info@kessaltortho-example.com
www.kessaltortho-example.com
Looking for letterhead, envelopes, business card, presentation folder
Would like a map of the two office locations in relation to each other. Have a business card with a map image if needed.

```html
<!DOCTYPE html>
<html lang="en">
<head>
<meta charset="utf-8">
<title>Kessalt Orthodontics Stationery</title>
<link rel="stylesheet" href="https://fonts.googleapis.com/css2?family=Libre+Baskerville:wght@400;700&family=Open+Sans:wght@400;700&display=swap">
<style>
  :root {
    --navy: #1b2a6b;
    --sky: #5b8fd2;
    --paper: #ffffff;
    --ink: #3b3b3b;
    --grey: #b9bcc4;
    --backdrop: #e7e4df;
  }
  * { margin: 0; padding: 0; box-sizing: border-box; }
  html, body { width: 1200px; height: 883px; overflow: hidden; }
  body { background: var(--backdrop); font-family: "Open Sans", Arial, sans-serif; color: var(--ink); position: relative; }

  .sheet { position: absolute; background: var(--paper); box-shadow: 0 3px 10px rgba(0,0,0,.18); overflow: hidden; }
  .sheet svg.decor { position: absolute; inset: 0; width: 100%; height: 100%; }

  .envelope-back { left: 48px; top: 53px; width: 545px; height: 259px; }
  .envelope-front { left: 48px; width: 545px; height: 257px; }
  .envelope-front.main-office { top: 319px; }
  .envelope-front.second-office { top: 593px; }
  .letterhead { left: 614px; top: 53px; width: 535px; height: 799px; }

  .brand { position: absolute; }
  .brand-name { font-family: "Libre Baskerville", Georgia, serif; font-weight: 700; color: var(--navy); line-height: 1; display: flex; align-items: center; gap: 8px; white-space: nowrap; }
  .brand-name .dot { width: 14px; height: 14px; border-radius: 50%; background: var(--sky); flex: none; }
  .brand-doctor { font-family: "Libre Baskerville", Georgia, serif; color: var(--navy); letter-spacing: .32em; text-transform: uppercase; margin-top: 7px; white-space: nowrap; }

  .envelope-front .brand { left: 30px; top: 22px; }
  .envelope-front .brand-name { font-size: 24px; }
  .envelope-front .brand-doctor { font-size: 8px; padding-left: 22px; }
  .return-address { position: absolute; left: 30px; top: 96px; font-size: 8px; white-space: nowrap; }

  .flap-mark { position: absolute; left: 0; right: 0; top: 22px; text-align: center; font-family: "Libre Baskerville", Georgia, serif; font-weight: 700; color: var(--paper); font-size: 13px; }
  .contact-line { position: absolute; font-size: 7.5px; white-space: nowrap; }
  .contact-line b { font-weight: 700; }
  .contact-line .sep { color: var(--grey); margin: 0 4px; }
  .envelope-back .contact-line { right: 34px; top: 240px; }

  .letterhead .brand { left: 40px; top: 28px; }
  .letterhead .brand-name { font-size: 32px; }
  .letterhead .brand-doctor { font-size: 9.5px; padding-left: 24px; }
  .offices { position: absolute; left: 22px; top: 612px; display: flex; font-size: 8px; line-height: 1.45; }
  .offices .office + .office { border-left: 1px solid var(--grey); margin-left: 12px; padding-left: 12px; }
  .letterhead .contact-line { left: 22px; top: 653px; }
</style>
</head>
<body>

<section class="sheet envelope-back">
  <svg class="decor" viewBox="0 0 545 259" preserveAspectRatio="none" aria-hidden="true">
    <path d="M0 0 H545 V60 C400 84 150 84 0 60 Z" fill="var(--navy)"/>
    <path d="M0 62 C150 86 400 86 545 62 V72 C400 94 150 94 0 72 Z" fill="var(--grey)" opacity=".55"/>
  </svg>
  <div class="flap-mark">Kessalt Orthodontics</div>
  <p class="contact-line"><b>Phone:</b> (555) 014-2267<span class="sep">|</span><b>Email:</b> info@kessaltortho-example.com<span class="sep">|</span><b>Web:</b> www.kessaltortho-example.com</p>
</section>

<section class="sheet envelope-front main-office">
  <svg class="decor" viewBox="0 0 545 257" preserveAspectRatio="none" aria-hidden="true">
    <path d="M0 10 C12 30 16 62 8 96 L0 100 Z" fill="var(--navy)"/>
    <path d="M13 16 C24 40 24 74 12 104" fill="none" stroke="var(--sky)" stroke-width="2"/>
    <path d="M545 70 C543 170 503 238 408 257 H545 Z" fill="var(--navy)"/>
    <path d="M535 80 C530 172 490 232 394 257" fill="none" stroke="var(--sky)" stroke-width="3"/>
  </svg>
  <div class="brand">
    <div class="brand-name"><span class="dot"></span>Kessalt Orthodontics</div>
    <div class="brand-doctor">Marcus Kessalt, DMD</div>
  </div>
  <p class="return-address">4183 Harlow Crest Dr., #210, Marlow Bay, CA 95871</p>
</section>

<section class="sheet envelope-front second-office">
  <svg class="decor" viewBox="0 0 545 257" preserveAspectRatio="none" aria-hidden="true">
    <path d="M0 10 C12 30 16 62 8 96 L0 100 Z" fill="var(--navy)"/>
    <path d="M13 16 C24 40 24 74 12 104" fill="none" stroke="var(--sky)" stroke-width="2"/>
    <path d="M545 70 C543 170 503 238 408 257 H545 Z" fill="var(--navy)"/>
    <path d="M535 80 C530 172 490 232 394 257" fill="none" stroke="var(--sky)" stroke-width="3"/>
  </svg>
  <div class="brand">
    <div class="brand-name"><span class="dot"></span>Kessalt Orthodontics</div>
    <div class="brand-doctor">Marcus Kessalt, DMD</div>
  </div>
  <p class="return-address">6452 Bramwell-Tusk Rd., #B, Ashford Glen, CA 95683</p>
</section>

<section class="sheet letterhead">
  <svg class="decor" viewBox="0 0 535 799" preserveAspectRatio="none" aria-hidden="true">
    <path d="M0 40 C14 80 18 150 8 210 L0 216 Z" fill="var(--navy)"/>
    <path d="M14 46 C28 90 28 160 14 222" fill="none" stroke="var(--sky)" stroke-width="2.5"/>
    <path d="M535 690 C526 745 496 785 446 799 H535 Z" fill="var(--navy)"/>
    <path d="M526 694 C516 748 484 786 432 799" fill="none" stroke="var(--sky)" stroke-width="3"/>
  </svg>
  <div class="brand">
    <div class="brand-name"><span class="dot"></span>Kessalt Orthodontics</div>
    <div class="brand-doctor">Marcus Kessalt, DMD</div>
  </div>
  <div class="offices">
    <p class="office">4183 Harlow Crest Dr., #210<br>Marlow Bay, CA 95871</p>
    <p class="office">6452 Bramwell-Tusk Rd., #B<br>Ashford Glen, CA 95683</p>
  </div>
  <p class="contact-line"><b>Phone:</b> (555) 014-2267<span class="sep">|</span><b>Email:</b> info@kessaltortho-example.com<span class="sep">|</span><b>Web:</b> www.kessaltortho-example.com</p>
</section>

</body>
</html>
```